Business Card Design Project

Financial planning, Insurance and Real estate - Financial Services company

Contact Information for Business Card

Looking for something simple in design -
Tolverin Equity LLC
Tolverin Wealth Managment

```html
<!DOCTYPE html>
<html lang="en">
<head>
<meta charset="utf-8">
<title>Tolverin Wealth Management — Business Card</title>
<link href="https://fonts.googleapis.com/css2?family=Oswald:wght@500;700&family=Open+Sans:wght@400;600&display=swap" rel="stylesheet">
<style>
  :root {
    --page-bg: #e9e6e1;
    --card-black: #070707;
    --card-sheen: #2a2a2a;
    --brand-blue: #3fb0dc;
    --text-white: #f2f2f2;
    --rule-white: #e6e6e6;
  }
  html, body {
    margin: 0;
    width: 1200px;
    height: 1023px;
    overflow: hidden;
    background: var(--page-bg);
  }
  .stage {
    width: 1200px;
    height: 1023px;
    display: flex;
    align-items: center;
    justify-content: center;
  }
  .card {
    position: relative;
    width: 840px;
    height: 480px;
    border-radius: 18px;
    background: radial-gradient(ellipse at 38% 45%, var(--card-sheen) 0%, var(--card-black) 62%);
    box-shadow: 0 18px 40px rgba(0,0,0,0.25);
    overflow: hidden;
  }
  .card__edge {
    position: absolute;
    right: 0; top: 0; bottom: 0;
    width: 10px;
    background: var(--brand-blue);
  }
  .brand {
    position: absolute;
    left: 70px;
    top: 0; bottom: 0;
    width: 300px;
    display: flex;
    flex-direction: column;
    align-items: center;
    justify-content: center;
    gap: 22px;
  }
  .brand__dot {
    width: 22px;
    height: 22px;
    border-radius: 50%;
    background: var(--brand-blue);
  }
  .brand__name {
    font-family: "Oswald", sans-serif;
    font-weight: 700;
    font-size: 24px;
    color: var(--brand-blue);
    letter-spacing: 0.3px;
    text-align: center;
  }
  .divider {
    position: absolute;
    left: 405px;
    top: 110px;
    width: 2px;
    height: 250px;
    background: var(--rule-white);
  }
  .details {
    position: absolute;
    left: 445px;
    top: 112px;
    width: 370px;
  }
  .details__name {
    margin: 0;
    font-family: "Oswald", sans-serif;
    font-weight: 700;
    font-size: 50px;
    line-height: 1;
    color: var(--brand-blue);
    letter-spacing: 0.5px;
    text-transform: uppercase;
  }
  .details__role {
    margin: 8px 0 0;
    font-family: "Open Sans", sans-serif;
    font-size: 19px;
    color: var(--text-white);
  }
  .details__dash {
    width: 22px;
    height: 2px;
    background: var(--brand-blue);
    margin: 22px 0 18px;
  }
  .contact {
    list-style: none;
    margin: 0;
    padding: 0;
    font-family: "Open Sans", sans-serif;
    font-size: 17px;
    color: var(--text-white);
  }
  .contact__item {
    display: flex;
    align-items: center;
    gap: 12px;
    margin-bottom: 9px;
  }
  .contact__icon {
    width: 14px;
    height: 14px;
    flex: none;
  }
</style>
</head>
<body>
<main class="stage">
  <article class="card">
    <div class="card__edge"></div>

    <section class="brand">
      <span class="brand__dot"></span>
      <span class="brand__name">Tolverin Wealth Management</span>
    </section>

    <div class="divider"></div>

    <section class="details">
      <h1 class="details__name">Daniel Reeve</h1>
      <p class="details__role">Director</p>
      <div class="details__dash"></div>
      <ul class="contact">
        <li class="contact__item">
          <svg class="contact__icon" viewBox="0 0 14 14" aria-hidden="true">
            <path d="M3 1 L5 4 L4 5.5 C5 7.5 6.5 9 8.5 10 L10 9 L13 11 L11.5 13 C6 12.5 1.5 8 1 2.5 Z" fill="#f2f2f2"/>
          </svg>
          <span>+64 21 555 01427</span>
        </li>
        <li class="contact__item">
          <svg class="contact__icon" viewBox="0 0 14 14" aria-hidden="true">
            <rect x="1" y="3" width="12" height="8" fill="none" stroke="#f2f2f2" stroke-width="1.4"/>
            <path d="M1 3 L7 8 L13 3" fill="none" stroke="#f2f2f2" stroke-width="1.4"/>
          </svg>
          <span>Tolverin@tolverinwealth.com</span>
        </li>
        <li class="contact__item">
          <svg class="contact__icon" viewBox="0 0 14 14" aria-hidden="true">
            <circle cx="7" cy="7" r="5.8" fill="none" stroke="#f2f2f2" stroke-width="1.3"/>
            <ellipse cx="7" cy="7" rx="2.5" ry="5.8" fill="none" stroke="#f2f2f2" stroke-width="1.1"/>
            <line x1="1.2" y1="7" x2="12.8" y2="7" stroke="#f2f2f2" stroke-width="1.1"/>
          </svg>
          <span>Tolverinwealthmanagment.com</span>
        </li>
      </ul>
    </section>
  </article>
</main>
</body>
</html>
```